Postcard needed for expert witness service

Looking for a professional postcard that will be mailed to personal injury lawyers / law firms to introduce my expert witness services.

Target Market(s)

Law firms, personal injury lawyers

Industry/Entity Type

Expert witness, law

Font styles to use
Sans Serif

Requirements
Must have
• Logo: The Frost Counsel [Main Heading]Do you handle snow and ice related slip and falls? Darrel is one of the top snow industry experts in the country! [Following should be in a list type fashion, possibly bulleted]Darrel's credentials: Accredited Winter Practitioner (AWP), past WRTA board member and chair, former ISO 9001 certified snow company owner , 32 years in the industry. (555) 284-3917 NOTES: Postcard will be 4" x 6" Please use both sides however must have room for labels and stamp
Should not have
• Wouldn't suggest using both photos on same side. Honestly, feel free to only use one of the slip and fall photos if it works out better. Thanks!

```html
<!DOCTYPE html>
<html lang="en">
<head>
<meta charset="utf-8">
<title>The Frost Counsel – Postcard</title>
<link href="https://fonts.googleapis.com/css2?family=Montserrat:wght@400;500;600;700&display=swap" rel="stylesheet">
<style>
  :root {
    --backdrop: #9b9b9b;
    --card: #ffffff;
    --ink: #1a1a1a;
    --band: #111111;
    --panel: #dedede;
    --line: #8a8a8a;
    --bullet: #777777;
    --photo-light: #c9c6c2;
    --photo-mid: #7d7f86;
    --photo-dark: #3f4552;
  }
  * { box-sizing: border-box; margin: 0; padding: 0; }
  html, body { width: 880px; height: 1200px; overflow: hidden; }
  body {
    background: var(--backdrop);
    font-family: "Montserrat", Arial, sans-serif;
    color: var(--ink);
    position: relative;
  }
  .postcard {
    position: absolute;
    left: 82px;
    width: 715px;
    height: 489px;
    background: var(--card);
    overflow: hidden;
    box-shadow: 0 2px 6px rgba(0,0,0,0.25);
  }
  .postcard--front { top: 82px; }
  .postcard--back { top: 624px; }
  .shapes { position: absolute; inset: 0; width: 100%; height: 100%; }

  /* Front */
  .brand {
    position: absolute;
    left: 400px;
    top: 125px;
    width: 250px;
    text-align: center;
    font-weight: 500;
    font-size: 34px;
    line-height: 1.15;
    letter-spacing: 1px;
    color: var(--ink);
  }
  .headline {
    position: absolute;
    right: 28px;
    top: 290px;
    width: 400px;
    text-align: right;
    font-size: 19px;
    font-weight: 500;
    line-height: 1.3;
    letter-spacing: 0.3px;
    text-transform: uppercase;
  }
  .headline strong { font-weight: 700; }
  .phone {
    position: absolute;
    left: 395px;
    top: 430px;
    display: flex;
    align-items: center;
    gap: 14px;
    color: #fff;
    font-size: 25px;
    letter-spacing: 4px;
    font-weight: 400;
  }
  .phone svg { width: 20px; height: 30px; }

  /* Back */
  .credentials {
    position: absolute;
    left: 42px;
    top: 225px;
    width: 310px;
  }
  .credentials h2 {
    font-size: 23px;
    font-weight: 700;
    margin-bottom: 16px;
  }
  .credentials ul { list-style: none; }
  .credentials li {
    position: relative;
    padding-left: 16px;
    font-size: 14px;
    line-height: 1.4;
    margin-bottom: 13px;
  }
  .credentials li::before {
    content: "";
    position: absolute;
    left: 0;
    top: 7px;
    width: 6px;
    height: 6px;
    border-radius: 50%;
    background: var(--bullet);
  }
  .credentials strong { font-weight: 700; }
  .mail-panel {
    position: absolute;
    left: 375px;
    top: 0;
    width: 340px;
    height: 100%;
    background: var(--panel);
  }
  .stamp-box {
    position: absolute;
    right: 38px;
    top: 32px;
    width: 78px;
    height: 84px;
    border: 1.5px solid var(--line);
  }
  .address-line {
    position: absolute;
    left: 40px;
    right: 30px;
    height: 1.5px;
    background: var(--line);
  }
</style>
</head>
<body>

<section class="postcard postcard--front">
  <svg class="shapes" viewBox="0 0 715 489" aria-hidden="true">
    <defs>
      <linearGradient id="slip-tones" x1="0" y1="0" x2="1" y2="1">
        <stop offset="0" stop-color="var(--photo-light)"/>
        <stop offset="0.55" stop-color="var(--photo-mid)"/>
        <stop offset="1" stop-color="var(--photo-dark)"/>
      </linearGradient>
    </defs>
    <path d="M0 0 H300 C250 60 250 120 300 170 C350 220 360 300 300 360 C270 390 260 440 250 489 H0 Z" fill="url(#slip-tones)"/>
    <path d="M250 489 C265 440 300 410 360 405 H715 V489 Z" fill="var(--band)"/>
  </svg>
  <div class="shapes" role="img" aria-label="Photo of a woman in winter clothing who has slipped and fallen on an icy pavement" style="width:300px;height:489px;"></div>

  <div class="brand">THE FROST<br>COUNSEL</div>

  <p class="headline">Do you handle <strong>snow</strong> and <strong>ice</strong> related slip and falls?</p>

  <div class="phone">
    <svg viewBox="0 0 20 30" aria-hidden="true"><rect x="2" y="1" width="16" height="28" rx="3" fill="none" stroke="#fff" stroke-width="2"/><line x1="8" y1="25" x2="12" y2="25" stroke="#fff" stroke-width="2"/></svg>
    <span>(555) 284-3917</span>
  </div>
</section>

<section class="postcard postcard--back">
  <svg class="shapes" viewBox="0 0 715 489" aria-hidden="true">
    <defs>
      <linearGradient id="fall-tones" x1="0" y1="0" x2="1" y2="1">
        <stop offset="0" stop-color="#d4d6da"/>
        <stop offset="0.5" stop-color="#5c6f93"/>
        <stop offset="1" stop-color="#2b3346"/>
      </linearGradient>
    </defs>
    <path d="M0 0 H360 C330 60 260 70 210 110 C160 150 100 170 0 165 Z" fill="var(--band)"/>
    <circle cx="145" cy="110" r="92" fill="#fff"/>
    <circle cx="145" cy="110" r="86" fill="url(#fall-tones)" role="img" aria-label="Photo of a man in work clothes falling on an icy surface"/>
  </svg>

  <div class="credentials">
    <h2>Darrel's credentials:</h2>
    <ul>
      <li>Accredited Winter Practitioner (AWP)</li>
      <li>Past <strong>WRTA</strong> Board Member And Chair</li>
      <li>Former <strong>Iso 9001</strong> Certified Snow Company Owner</li>
      <li><strong>32</strong> Years In The Industry</li>
    </ul>
  </div>

  <div class="mail-panel">
    <div class="stamp-box"></div>
    <div class="address-line" style="top:220px"></div>
    <div class="address-line" style="top:272px"></div>
    <div class="address-line" style="top:324px"></div>
    <div class="address-line" style="top:376px"></div>
    <div class="address-line" style="top:428px"></div>
  </div>
</section>

</body>
</html>
```